Poster announcing University Web Analytics talk

We need a poster to announce an upcoming talk on Web Analytics at the local University. The event is addressed to final year students (mostly in Informatic Engineering, although other majors are wellcomed as well) who may be interested in specializing in this rising field.

The poster should present a brief list of the points we'll be addressing, as well as the place and time of the meeting. Also, it must feature our company logo (check the uploads section to find it) and our website url: http://www.brasslanternworks.net.

Texts for the poster:

Headline: "Get specialized in Web & Mobile Analytics"

Topics that will be covered:
- Introduction to Analytics, market, work opportunities
- Know the basics of an Analytics project: planning, phases, implementation
- Job bank: bring your CV!

Event information: "Thursday 20th June at the Escuela de Sistemas, Instituto Pelayo Norte". [A space to fill with the time must be provided here]

However, we'll be translating all the text to Spanish later, so we'll need a file where we can modify the text layers.
Updates

Thanks to all of you, we're receiving so many excellent works!

We had missed to include some important information on the brief - we didn't say anything about the colors, and we have been getting some designs based in dark colors. Now, it doesn't matter what colors you use, but we'd like better a brighter design (no matter if the color combination is more playful or either rather serious). This is going to be a free talk addressed to last year students, so we want to transmit a feeling of an interesting, easy and entertaining afternoon.

I hope these comments are helpful, please reach me with any question or comment. 

Thanks a lot again!
Nuria 
BL team

Target Market(s)

Final year students and graduates.

Industry/Entity Type

Bank

Requirements
Must have
• Design must be submitted in vector format, preferably .psd. We must be able to modify the text layers. Our logo (check the files section) and website url (http://www.brasslanternworks.net) must be included
Nice to have
• Illustrations making reference to Analytics (charts, statistics, code) and/or the internet will be a plus!

```html
<!DOCTYPE html>
<html lang="en">
<head>
<meta charset="utf-8">
<title>Get specialized in Web &amp; Mobile Analytics</title>
<link href="https://fonts.googleapis.com/css2?family=Arvo:wght@400;700&family=Montserrat:wght@300;400&display=swap" rel="stylesheet">
<style>
  :root {
    --paper: #ffffff;
    --ink: #333333;
    --accent-red: #e1251b;
    --brand-blue: #1d5f86;
    --brand-green: #8cc63f;
    --muted: #444444;
  }
  html, body {
    margin: 0;
    padding: 0;
    overflow: hidden;
    background: var(--paper);
  }
  .poster {
    position: relative;
    width: 849px;
    height: 1200px;
    overflow: hidden;
    background: var(--paper);
    color: var(--ink);
    font-family: "Montserrat", Arial, sans-serif;
  }
  .brand {
    position: absolute;
    top: 78px;
    right: 54px;
    display: flex;
    align-items: center;
    gap: 12px;
  }
  .brand-mark {
    width: 40px;
    height: 40px;
    background: var(--brand-green);
  }
  .brand-name {
    font-family: "Arvo", Georgia, serif;
    font-weight: 400;
    font-size: 30px;
    line-height: 1;
    color: var(--brand-blue);
  }
  .headline {
    position: absolute;
    left: 81px;
    top: 222px;
    margin: 0;
    font-weight: 300;
  }
  .headline-lead {
    display: block;
    font-family: "Montserrat", Arial, sans-serif;
    font-weight: 300;
    font-size: 44px;
    line-height: 54px;
    color: var(--ink);
  }
  .headline-topic {
    display: block;
    font-family: "Arvo", Georgia, serif;
    font-weight: 700;
    font-size: 47px;
    line-height: 60px;
    color: var(--accent-red);
  }
  .topics {
    position: absolute;
    left: 81px;
    top: 348px;
  }
  .topics-title {
    margin: 0 0 6px;
    font-family: "Arvo", Georgia, serif;
    font-weight: 700;
    font-size: 20px;
    line-height: 28px;
    color: var(--ink);
  }
  .topic-list {
    list-style: none;
    margin: 0;
    padding: 0;
  }
  .topic-item {
    position: relative;
    padding-left: 34px;
    font-family: "Arvo", Georgia, serif;
    font-size: 21px;
    line-height: 30px;
    color: var(--ink);
    margin-bottom: 7px;
  }
  .topic-arrow {
    position: absolute;
    left: 0;
    top: 9px;
    width: 20px;
    height: 14px;
  }
  .event {
    position: absolute;
    left: 81px;
    top: 555px;
    margin: 0;
    font-family: "Arvo", Georgia, serif;
    font-size: 21px;
    line-height: 30px;
    color: var(--muted);
  }
  .event strong {
    font-weight: 700;
    color: var(--accent-red);
  }
  .hero-art {
    position: absolute;
    left: 0;
    top: 630px;
    width: 740px;
    height: 570px;
  }
  .site-url {
    position: absolute;
    right: 54px;
    bottom: 26px;
    font-family: "Montserrat", Arial, sans-serif;
    font-size: 16px;
    color: var(--ink);
  }
</style>
</head>
<body>
<main class="poster">
  <div class="brand">
    <span class="brand-mark" aria-hidden="true"></span>
    <span class="brand-name">brass lantern works</span>
  </div>

  <h1 class="headline">
    <span class="headline-lead">Get specialized in</span>
    <span class="headline-topic">Web &amp; Mobile Analytics</span>
  </h1>

  <section class="topics">
    <h2 class="topics-title">Topics that will be covered:</h2>
    <ul class="topic-list">
      <li class="topic-item">
        <svg class="topic-arrow" viewBox="0 0 20 14" aria-hidden="true"><path d="M0 5h11V0l9 7-9 7V9H0z" fill="#333"/></svg>
        Introduction to Analytics, market, work opportunities
      </li>
      <li class="topic-item">
        <svg class="topic-arrow" viewBox="0 0 20 14" aria-hidden="true"><path d="M0 5h11V0l9 7-9 7V9H0z" fill="#333"/></svg>
        Know the basics of an Analytics project:<br>Planning, phases, implementation
      </li>
      <li class="topic-item">
        <svg class="topic-arrow" viewBox="0 0 20 14" aria-hidden="true"><path d="M0 5h11V0l9 7-9 7V9H0z" fill="#333"/></svg>
        Job bank: bring your CV!
      </li>
    </ul>
  </section>

  <p class="event">
    On <strong>Thursday 20th June</strong><br>
    At <strong>The Escuela de Sistemas</strong><br>
    Instituto Pelayo Norte
  </p>

  <svg class="hero-art" viewBox="0 0 740 570" role="img" aria-label="Illustration of a tablet showing a rising red trend arrow and colourful 3D bar chart from yellow to red over data tables">
    <defs>
      <linearGradient id="heroTone" x1="0" y1="1" x2="1" y2="0">
        <stop offset="0" stop-color="#2b2d31"/>
        <stop offset="0.35" stop-color="#9fb8d0"/>
        <stop offset="0.6" stop-color="#d9e37a"/>
        <stop offset="0.8" stop-color="#f3a13a"/>
        <stop offset="1" stop-color="#e1251b"/>
      </linearGradient>
    </defs>
    <polygon points="0,240 700,60 720,530 0,570" fill="url(#heroTone)"/>
  </svg>

  <span class="site-url">www.brasslanternworks.net</span>
</main>
</body>
</html>
```